Web Design for a recruitment company

Website is for a recruitment company, with a particular focus on temporary staff, trades, skilled, and unskilled labour markets. Website will consist of a home page design and separate design for additional pages. Website will be implemented as a template in SharePoint. There is a separate design project for a new logo and look colours will need to be co-ordinated.

Target Market(s)

Company executives in the construction and trades areas looking for staff. Trades people, skilled and unskilled labourers looking for work.

Industry/Entity Type

It Company

Number of Pages Required

2 page

Requirements
Must have
• Looking for Home Page design plus design for additional pages.
• .
Nice to have
• Right People | Right Place is the firms byline, company name is Voskin Staffing. They will be in the Logo (separate project) but may also appear elsewhere in the design.
• Company values (attached file) may be reflected in the design where practical.

```html
<!DOCTYPE html>
<html lang="en">
<head>
<meta charset="utf-8">
<title>Voskin Staffing – Home</title>
<link rel="stylesheet" href="https://fonts.googleapis.com/css2?family=Open+Sans:wght@400;600;700&family=Roboto+Condensed:wght@400&family=Roboto:wght@400&display=swap">
<style>
:root{
  --green:#5aab2e;
  --ink:#222;
  --text:#444;
  --panel:#f4f4f4;
  --footer:#2c2c30;
  --footer-text:#8a8a90;
  --accent:#e0461e;
  --white:#fff;
}
*{margin:0;padding:0;box-sizing:border-box}
html,body{width:878px;height:1200px;overflow:hidden;background:var(--white)}
body{position:relative;font-family:"Open Sans",Arial,sans-serif;color:var(--text)}

/* header */
.site-header{position:absolute;left:0;top:0;width:878px;height:40px;background:var(--white);box-shadow:0 1px 3px rgba(0,0,0,.2);z-index:2}
.brand{position:absolute;left:116px;top:5px;display:flex;align-items:center;gap:8px}
.brand-dot{width:26px;height:26px;border-radius:50%;background:#555}
.brand-name{font-weight:700;font-size:16px;color:var(--ink);line-height:16px}
.brand-tag{font-size:8.5px;color:#333;line-height:12px}
.main-nav a{position:absolute;top:0;height:40px;line-height:42px;font-size:8.5px;color:#333;text-decoration:none}
.main-nav a.active{background:var(--green);color:var(--white);padding:0 8px;left:478px}

/* hero */
.hero{position:absolute;left:0;top:40px;width:878px;height:280px;background:linear-gradient(180deg,#2b5fae 0%,#4d86c9 55%,#8aa9c6 100%);border-bottom:2px solid var(--green)}
.hero-quote{position:absolute;left:116px;background:rgba(0,0,0,.75);color:var(--white);font-size:16px;padding:0 7px;height:28px;line-height:28px;white-space:nowrap}
.hero-quote b{font-weight:700}
.hero-sub{position:absolute;left:116px;top:194px;width:326px;height:29px;background:rgba(255,255,255,.85);font-size:8.8px;color:#333;line-height:29px;padding-left:10px;white-space:nowrap;overflow:hidden}
.hero-btn{position:absolute;left:116px;top:228px;width:72px;height:22px;background:var(--white);font-size:7.5px;line-height:22px;text-align:center;color:#333}
.dots span{position:absolute;top:262px;width:7px;height:7px;border-radius:50%;background:rgba(255,255,255,.5)}

/* welcome */
.welcome-title{position:absolute;top:342px;width:878px;text-align:center;color:var(--green);font-weight:700;font-size:18px}
.welcome-text{position:absolute;top:371px;width:878px;text-align:center;font-size:8.5px;color:#444}

/* services */
.service{position:absolute;top:419px;width:219px;height:108px;background:var(--panel)}
.service h3{position:absolute;left:11px;top:15px;font-weight:400;font-size:10.4px;color:var(--ink)}
.service .rule{position:absolute;left:8px;right:8px;top:35px;height:1px;background:var(--green)}
.service svg{position:absolute;left:8px;top:43px}
.service p{position:absolute;left:63px;top:47px;width:150px;font-family:Arial,sans-serif;font-size:6.8px;line-height:11px;color:#777}
.service .tag{position:absolute;right:8px;top:82px;background:var(--green);color:var(--white);font-family:Arial,sans-serif;font-size:7px;padding:1px 3px}

/* about */
.about-photo{position:absolute;left:116px;top:569px;width:185px;height:106px;background:linear-gradient(180deg,#2f6fb8 0%,#6f9cc9 45%,#9a7a52 60%,#6e5334 100%)}
.about-title{position:absolute;left:322px;top:563px;font-size:15px;font-weight:400;color:var(--green)}
.about-text{position:absolute;left:322px;top:592px;width:430px;font-size:7.3px;line-height:11.5px;color:#333}
.read-more{position:absolute;left:322px;top:658px;width:69px;height:16px;background:#111;color:var(--white);font-size:7.5px;line-height:16px;text-align:center}

/* solutions */
.solution{position:absolute;top:714px;width:192px}
.solution .photo{width:192px;height:94px}
.solution h4{margin-top:10px;font-family:"Roboto Condensed",sans-serif;font-weight:400;font-size:11px;color:#3b4a5a}
.solution p{margin-top:5px;font-size:7px;line-height:11px;color:#444}

/* news */
.news{position:absolute;left:130px;top:912px;width:630px;height:33px;border-top:1px solid #e4e4e4;border-bottom:1px solid #e4e4e4;font-family:Roboto,sans-serif}
.news .label{position:absolute;left:1px;top:10px;font-size:9.5px;color:#999}
.news .date{position:absolute;left:73px;top:11px;font-size:7.5px;color:#999}
.news .headline{position:absolute;left:122px;top:11px;font-size:7.5px;color:var(--accent)}
.news svg{position:absolute;right:4px;top:7px}

/* footer */
.site-footer{position:absolute;left:0;top:976px;width:878px;height:224px;background:var(--footer)}
.foot-col{position:absolute;top:20px}
.foot-col h5{font-weight:400;font-size:11px;color:#e8e8e8;margin-bottom:12px}
.foot-col li{list-style:none;font-size:7.5px;color:var(--footer-text);height:20px}
.social{position:absolute;top:113px}
.social span{position:absolute;width:20px;height:20px;border-radius:50%;border:1px solid #6a6a70}
.copyright{position:absolute;left:116px;top:169px;font-size:7px;color:var(--footer-text)}
.legal{position:absolute;right:99px;top:169px;font-size:7px;color:var(--footer-text);word-spacing:2px}
.foot-rule{position:absolute;left:116px;width:666px;top:202px;height:1px;background:#3d3d42}
</style>
</head>
<body>

<header class="site-header">
  <div class="brand">
    <div class="brand-dot"></div>
    <div>
      <div class="brand-name">Voskin Staffing</div>
      <div class="brand-tag">Right People | Right Place</div>
    </div>
  </div>
  <nav class="main-nav">
    <a class="active">Home</a>
    <a style="left:527px">About Us</a>
    <a style="left:582px">Jobs</a>
    <a style="left:614px">Career</a>
    <a style="left:656px">Work</a>
    <a style="left:692px">Site Map</a>
    <a style="left:742px">Contact Us</a>
  </nav>
</header>

<section class="hero" role="img" aria-label="Two construction workers in hard hats and high-visibility vests beside a steel building frame under a blue sky"></section>
<div class="hero-quote" style="top:140px">“<b>EVERYONE</b> CAN MAKE</div>
<div class="hero-quote" style="top:166px">A <b>DIFFERENCE</b>, AND <b>EVERY ONE CAN WORK</b>”</div>
<div class="hero-sub">Sit wuetma met lipsum lroem ipsum door sit amet lipsum dolor sit amet lips</div>
<div class="hero-btn">MORE DETAILS</div>
<div class="dots">
  <span style="left:116px;background:#fff"></span>
  <span style="left:131px"></span>
  <span style="left:143px"></span>
  <span style="left:155px"></span>
</div>

<h1 class="welcome-title">Welcome To Voskin Staffing</h1>
<p class="welcome-text">Sed ut perspiciatis unde omnis iste natus error sit voluptatem accusantium doloremque laudantium, totam rem aperiam, eaque ipsa quae a</p>

<div class="service" style="left:119px">
  <h3>Sit Quet amet lipsum dolor</h3><div class="rule"></div>
  <svg width="46" height="46" viewBox="0 0 46 46"><circle cx="23" cy="23" r="21" fill="#111" stroke="var(--green)" stroke-width="3"/><circle cx="23" cy="23" r="7" fill="none" stroke="#fff" stroke-width="3"/><g stroke="#fff" stroke-width="3"><line x1="23" y1="11" x2="23" y2="15"/><line x1="23" y1="31" x2="23" y2="35"/><line x1="11" y1="23" x2="15" y2="23"/><line x1="31" y1="23" x2="35" y2="23"/><line x1="15" y1="15" x2="18" y2="18"/><line x1="28" y1="28" x2="31" y2="31"/><line x1="31" y1="15" x2="28" y2="18"/><line x1="15" y1="31" x2="18" y2="28"/></g></svg>
  <p>We create modern, creative and functional website that you can easily manage yourself in CMS your website.</p>
  <span class="tag">We create original web</span>
</div>
<div class="service" style="left:339px">
  <h3>Sit Quet amet lipsum dolor</h3><div class="rule"></div>
  <svg width="46" height="46" viewBox="0 0 46 46"><circle cx="23" cy="23" r="21" fill="#111" stroke="var(--green)" stroke-width="3"/><rect x="12" y="17" width="22" height="15" rx="2" fill="#fff"/><rect x="19" y="13" width="8" height="5" fill="none" stroke="#fff" stroke-width="2"/><circle cx="23" cy="24.5" r="5" fill="#111"/><text x="23" y="27.5" font-size="8" fill="#fff" text-anchor="middle" font-family="Arial">$</text></svg>
  <p>We create online store and easy to use and packed with many features that will support your sales.</p>
  <span class="tag">Boot your Internet sales</span>
</div>
<div class="service" style="left:558px">
  <h3>Sit Quet amet lipsum dolor</h3><div class="rule"></div>
  <svg width="46" height="46" viewBox="0 0 46 46"><circle cx="23" cy="23" r="21" fill="#111" stroke="var(--green)" stroke-width="3"/><g stroke="#fff" stroke-width="2.5" stroke-linecap="round"><line x1="14" y1="32" x2="30" y2="16"/><line x1="16" y1="14" x2="32" y2="30"/><line x1="26" y1="13" x2="33" y2="20"/></g></svg>
  <p>Top position of your web pages in search engines - SEO, PPC advertising, newsletter, copywriting, social, local, ...</p>
  <span class="tag">We get your site to the top</span>
</div>

<div class="about-photo" role="img" aria-label="Surveyor in a hard hat using a tripod level on an earthworks site with a bulldozer"></div>
<h2 class="about-title">About Our Company</h2>
<p class="about-text">Sed ut perspiciatis unde omnis iste natus error sit voluptatem accusantium doloremque laudantium, totam rem aperiam, eaque ipsa quae allo inven tore veritatis et quasi architecto beatae vitae dicta sunt explicabo. Nemo enim ipsam voluptatem quia voluptas sit aspernatur aut odit aut fugit,<br>sed quia consequuntur magni dolores eos qui ratione voluptatem sequi nesciunt. Neque porro quisquam est, qui dolorem ipsum quia dolor sit amet, consectetur, adipisci velit, sed quia non numquaSed ut perspiciatis unde omnis iste natus error</p>
<div class="read-more">Read More</div>

<article class="solution" style="left:125px">
  <div class="photo" role="img" aria-label="Builders reviewing plans inside a timber roof frame" style="background:linear-gradient(160deg,#c08a4e,#8a5a2e 60%,#3f6fa8)"></div>
  <h4>Business Process Outsourcing</h4>
  <p>Lorem ipsum dolorSit amet consecteturAdipiscing elit,<br>ed do euismodTempor incidunt Labore et dolor<br>Magna aliqua.Lorem ipsum dolorSit amet consecteturAd-<br>ipscing elit,ed do euismodTempor incidunt</p>
</article>
<article class="solution" style="left:352px">
  <div class="photo" role="img" aria-label="Engineers in hard hats inspecting a demolition site" style="background:linear-gradient(180deg,#7f9fc4,#b7bfc4 45%,#7a7060)"></div>
  <h4>App. Development &amp; Maintenance</h4>
  <p>Lorem ipsum dolorSit amet consecteturAdipiscing elit,<br>ed do euismodTempor incidunt Labore et dolor<br>Magna aliqua.Lorem ipsum dolorSit amet consecteturAd-<br>ipscing elit,ed do euismodTempor incidunt</p>
</article>
<article class="solution" style="left:570px">
  <div class="photo" role="img" aria-label="Modern steel boat lift structure against a cloudy sky" style="background:linear-gradient(180deg,#5d86c0,#c5cfd9 55%,#6f9a4e)"></div>
  <h4>Human Capital Management Solution</h4>
  <p>Lorem ipsum dolorSit amet consecteturAdipiscing elit,<br>ed do euismodTempor incidunt Labore et dolor<br>Magna aliqua.Lorem ipsum dolorSit amet consecteturAd-<br>ipscing elit,ed do euismodTempor incidunt</p>
</article>

<div class="news">
  <span class="label">LATEST NEWS:</span>
  <span class="date">June 3, 2013</span>
  <span class="headline">Northgate Builders has signed up with Harlow Works Ltd</span>
  <svg width="36" height="18" viewBox="0 0 36 18"><path d="M8 2 L2 9 L8 16" fill="none" stroke="var(--accent)" stroke-width="1.8"/><line x1="18" y1="1" x2="18" y2="17" stroke="#ddd"/><path d="M28 2 L34 9 L28 16" fill="none" stroke="var(--accent)" stroke-width="1.8"/></svg>
</div>

<footer class="site-footer">
  <div class="foot-col" style="left:119px"><h5>Info</h5><ul><li>Book A Demo</li><li>Products</li><li>Features</li><li>FAQ</li><li>API Documentation</li></ul></div>
  <div class="foot-col" style="left:247px"><h5>Email</h5><ul><li>hello@voskinmail.example</li></ul></div>
  <div class="foot-col" style="left:373px"><h5>Company</h5><ul><li>Careers</li></ul></div>
  <div class="foot-col" style="left:498px"><h5>Contact Us</h5><ul><li>Millbrook Enterprise Hub</li><li>Quarry Lane</li><li>Easton</li><li>EA4 2QT</li><li>Call Us: 0800 555 0192</li></ul></div>
  <div class="social">
    <span style="left:674px"></span><span style="left:702px"></span><span style="left:730px"></span><span style="left:757px"></span>
  </div>
  <div class="copyright">©copyright2014. All Rights Reserved</div>
  <div class="legal">Privacy Policy &nbsp; Terms and Conditions</div>
  <div class="foot-rule"></div>
</footer>

</body>
</html>
```